Bright Pelvic Health Business Card

Need a business card for a surgical practice called Bright Pelvic Health. We have recently selected a logo (attached). The business card will need to have two formats:
1) One with the logo/physician name/ contact info on the front and location information on the back.
2) One in "appointment reminder card" style with the logo/ contact info/ date/ time on the front and the location information on the back.

The front side should include the following information:
- Logo
- Ravi K. Desai, MD FACOG
- phone: 469-555-0182
- fax: 1-469-555-0147
- email: admin@brightpelvic.example
- website: www.brightpelvichealth.example

The back side should have the office locations listed:
4812 Quarry Bend Dr, Plano, TX 75093
3650 Wrenfield Rd, Plano, TX 75025
2245 Brambleton Ln, Irving, TX 75038
915 S Garnet Ave B314, Dallas, TX 75201
1836 Tillman Pkwy, Grand Prairie, TX 75051
6417 Dorrance Way Dr, San Antonio, TX 78240
5920 Kessler Rd, Pasadena, TX 77504

Target Market(s)

1. Other physicians who might refer patients
2. Female patients

Industry/Entity Type

Business

Font styles to use
Other font styles liked:
• Tahoma for lettering

Requirements
Must have
• As per the instructions
Should not have
• No other images needed -- please try to keep font consistent with logo design. Can use Tahoma as the font for lettering.

```html
<!DOCTYPE html>
<html lang="en">
<head>
<meta charset="utf-8">
<title>Bright Pelvic Health – Business Cards</title>
<link href="https://fonts.googleapis.com/css2?family=PT+Sans:wght@400;700&display=swap" rel="stylesheet">
<style>
  :root {
    --navy: #1d3c70;
    --deep-blue: #17529e;
    --mid-blue: #2a86d0;
    --light-blue: #5ec2f0;
    --teal: #2fa6b8;
    --white: #ffffff;
    --stage: #e8ebef;
    --rule: #9fb3c8;
  }
  * { box-sizing: border-box; margin: 0; padding: 0; }
  html, body {
    width: 1200px; height: 793px; overflow: hidden;
    background: var(--stage);
    font-family: "PT Sans", Tahoma, sans-serif;
  }
  .sheet { position: relative; width: 1200px; height: 793px; }

  .card {
    position: absolute; width: 463px; height: 266px; overflow: hidden;
    background: radial-gradient(ellipse 70% 90% at 50% 35%, var(--light-blue) 0%, var(--mid-blue) 45%, var(--deep-blue) 100%);
    color: var(--white);
    box-shadow: 0 3px 8px rgba(0,0,0,.18);
  }
  .card--front-left  { left: 110px; top: 90px; }
  .card--front-right { left: 638px; top: 90px; }
  .card--back-left   { left: 110px; top: 417px; }
  .card--back-right  { left: 638px; top: 417px; }

  /* front */
  .brand-panel {
    position: absolute; left: 0; right: 0; top: 8px;
    background: var(--white);
    display: flex; align-items: center; justify-content: center; gap: 10px;
  }
  .brand-panel::after {
    content: ""; position: absolute; left: 50%; bottom: -15px; margin-left: -16px;
    border-left: 16px solid transparent; border-right: 16px solid transparent;
    border-top: 15px solid var(--white);
  }
  .card--front-left .brand-panel  { height: 120px; padding-top: 58px; }
  .card--front-right .brand-panel { height: 110px; padding-top: 52px; }
  .brand-dot { width: 14px; height: 14px; border-radius: 50%; background: var(--deep-blue); }
  .brand-name { font-size: 25px; font-weight: 700; color: var(--navy); letter-spacing: .3px; }

  .contact { position: absolute; left: 0; right: 0; text-align: center; }
  .card--front-left .contact { top: 148px; }
  .card--front-right .contact { top: 138px; }
  .physician { font-size: 17px; line-height: 20px; }
  .physician .credentials { font-size: 13px; }
  .specialty { font-size: 12px; line-height: 16px; }
  .card--front-right .specialty { font-size: 14px; line-height: 18px; }
  .contact-line { font-size: 12.5px; line-height: 19px; }
  .card--front-left .contact-lines { margin-top: 16px; }
  .contact-line b { font-weight: 700; }
  .contact-line span + span { margin-left: 18px; }

  .appointment {
    position: absolute; left: 18px; right: 18px; top: 221px; height: 31px;
    background: var(--white); display: flex; align-items: center;
    font-size: 11px; color: var(--navy);
  }
  .appointment-label {
    background: var(--teal); color: var(--white); font-weight: 700; font-size: 12.5px;
    height: 100%; display: flex; align-items: center; padding: 0 9px;
  }
  .appointment-field { display: flex; align-items: center; gap: 6px; margin-left: 9px; }
  .appointment-field--date { width: 130px; }
  .appointment-field--time { flex: 1; margin-left: 8px; }
  .appointment-line { flex: 1; border-bottom: 1px solid var(--rule); height: 9px; }
  .meridiem { display: flex; gap: 14px; margin: 0 10px 0 14px; font-size: 9px; }
  .meridiem span::before {
    content: ""; display: inline-block; width: 8px; height: 8px; border: 1px solid var(--navy);
    margin-right: 4px; vertical-align: -1px;
  }

  /* back */
  .locations-header {
    height: 68px; display: flex; align-items: center; justify-content: center;
    font-size: 22px; letter-spacing: 1px;
  }
  .locations-body {
    position: absolute; left: 0; right: 0; top: 68px; bottom: 17px;
    background: var(--white); padding: 12px 0 0 68px;
  }
  .locations-list { list-style: none; color: var(--navy); font-size: 15px; line-height: 23px; letter-spacing: .3px; }
  .locations-list li { position: relative; padding-left: 22px; }
  .locations-list li::before {
    content: ""; position: absolute; left: 0; top: 7px; width: 10px; height: 10px;
    border-radius: 50%; background: var(--navy);
  }
</style>
</head>
<body>
<main class="sheet">

  <section class="card card--front-left">
    <div class="brand-panel">
      <span class="brand-dot"></span>
      <span class="brand-name">Bright Pelvic Health</span>
    </div>
    <div class="contact">
      <p class="physician">Ravi K. Desai. <span class="credentials">MD FACOG</span></p>
      <p class="specialty">Female Pelvic Medicine &amp; Reconstructive Surgery</p>
      <div class="contact-lines">
        <p class="contact-line"><span><b>phone</b>: 469-555-0182</span><span><b>fax</b>: 1-469-555-0147</span></p>
        <p class="contact-line"><span><b>email</b>: admin@brightpelvic.example</span><span><b>website</b>: www.brightpelvichealth.example</span></p>
      </div>
    </div>
  </section>

  <section class="card card--front-right">
    <div class="brand-panel">
      <span class="brand-dot"></span>
      <span class="brand-name">Bright Pelvic Health</span>
    </div>
    <div class="contact">
      <p class="physician">Ravi K. Desai. <span class="credentials">MD FACOG</span></p>
      <p class="specialty">Female Pelvic Medicine &amp; Reconstructive Surgery</p>
      <p class="contact-line"><span>phone: 469-555-0182</span><span>fax: 1-469-555-0147</span></p>
      <p class="contact-line"><span>email: admin@brightpelvic.example</span><span>website: www.brightpelvichealth.example</span></p>
    </div>
    <div class="appointment">
      <span class="appointment-label">Appointment</span>
      <span class="appointment-field appointment-field--date">Date: <span class="appointment-line"></span></span>
      <span class="appointment-field appointment-field--time">Time: <span class="appointment-line"></span></span>
      <span class="meridiem"><span>am</span><span>pm</span></span>
    </div>
  </section>

  <section class="card card--back-left">
    <h2 class="locations-header">OFFICE LOCATIONS</h2>
    <div class="locations-body">
      <ul class="locations-list">
        <li>4812 Quarry Bend Dr, Plano, TX 75093</li>
        <li>3650 Wrenfield Rd, Plano, TX 75025</li>
        <li>2245 Brambleton Ln, Irving, TX 75038</li>
        <li>915 S Garnet Ave B314, Dallas, TX 75201</li>
        <li>1836 Tillman Pkwy, Grand Prairie, TX 75051</li>
        <li>6417 Dorrance Way Dr, San Antonio, TX 78240</li>
        <li>5920 Kessler Rd, Pasadena, TX 77504</li>
      </ul>
    </div>
  </section>

  <section class="card card--back-right">
    <h2 class="locations-header">OFFICE LOCATIONS</h2>
    <div class="locations-body">
      <ul class="locations-list">
        <li>4812 Quarry Bend Dr, Plano, TX 75093</li>
        <li>3650 Wrenfield Rd, Plano, TX 75025</li>
        <li>2245 Brambleton Ln, Irving, TX 75038</li>
        <li>915 S Garnet Ave B314, Dallas, TX 75201</li>
        <li>1836 Tillman Pkwy, Grand Prairie, TX 75051</li>
        <li>6417 Dorrance Way Dr, San Antonio, TX 78240</li>
        <li>5920 Kessler Rd, Pasadena, TX 77504</li>
      </ul>
    </div>
  </section>

</main>
</body>
</html>
```